Fairway Relief Rockets promotional cards (rack card)

This will be an eye catching (rack) card designed to be left at the Golf clubhouse with special event coordinators and emailed or physically handed to charities conducting fund raising golf tournaments. I need an electronic file version that I could email to prospects to view before they decide if they will help promote this to their tournament directors
Photos, logos, files and website link are attached. all photos on my website are available upon request.
www.fairwayreliefrockets.com
Target Market(s)
must be appealing to charities conducting golf tournaments as a method to raise funds,
Industry/Entity Type
Golf Course
Font styles to use
Other font styles liked:
- Screwed Oblique for any bold type, serif for body text
Requirements
Must have
- include a call to action to "book your event now"
- use the colors in my logo
- include the photo attached, could include additional photos from my website
- include "several packages to choose from"
- I would like this to be vectorized to be able to resize or shrink slightly as needed to fit printables.
Nice to have
- in the background of photos, there is a 7 foot pull up banner that participants often stand in front of to take videos and photos, you can incorporate that if possible as a watermark or background image. I can provide that original image if needed.
Should not have
- any salesy "car commercial" banners or balloons or stars or anything like that.

```html
<!DOCTYPE html>
<html lang="en">
<head>
<meta charset="utf-8">
<title>Fairway Relief Rockets – Rack Card</title>
<link href="https://fonts.googleapis.com/css2?family=Bebas+Neue&family=Open+Sans:ital,wght@0,400;0,700;1,400&display=swap" rel="stylesheet">
<style>
  :root {
    --green: #0f6b3b;
    --green-text: #137a3f;
    --orange: #f7941d;
    --white: #ffffff;
    --body-grey: #5a5a5a;
    --photo-dark: #1f2a1c;
    --photo-mid: #3f6a2c;
    --photo-light: #7fa84d;
  }
  * { box-sizing: border-box; margin: 0; padding: 0; }
  html, body { width: 924px; height: 1200px; overflow: hidden; background: var(--white); }
  .card { position: relative; width: 924px; height: 1200px; overflow: hidden; font-family: "Open Sans", Arial, sans-serif; color: var(--body-grey); }

  .brand { position: absolute; left: 0; top: 0; width: 296px; height: 220px; background: var(--white); }
  .brand-name { position: absolute; left: 30px; top: 18px; width: 250px; font-family: "Bebas Neue", Impact, sans-serif; color: var(--green-text); font-size: 50px; line-height: 46px; letter-spacing: 2px; }
  .brand-name span { display: block; }
  .brand-name span:nth-child(2) { padding-left: 36px; }
  .brand-name span:nth-child(3) { padding-left: 72px; }
  .brand-url { position: absolute; left: 0; width: 296px; top: 178px; text-align: center; font-family: Arial, Helvetica, sans-serif; font-weight: 700; font-size: 17px; color: var(--green-text); }

  .packages { position: absolute; left: 0; top: 220px; width: 296px; height: 690px; background: var(--green); color: var(--white); padding: 52px 14px 0 44px; }
  .packages-title { font-family: "Bebas Neue", Impact, sans-serif; font-weight: 400; line-height: 1; }
  .packages-title .big { display: block; font-size: 36px; letter-spacing: 1px; }
  .packages-title .small { display: block; font-size: 28px; margin-top: 6px; letter-spacing: 1px; }
  .option-list { list-style: none; margin-top: 44px; margin-left: -26px; }
  .option { position: relative; padding-left: 26px; font-size: 17.5px; line-height: 22px; margin-bottom: 22px; }
  .option svg { position: absolute; left: 0; top: 3px; width: 17px; height: 15px; }
  .option-label { color: var(--orange); }

  .booking { position: absolute; left: 0; top: 910px; width: 296px; height: 290px; background: var(--orange); color: var(--white); padding: 24px 10px 0 22px; }
  .booking-title { font-family: "Bebas Neue", Impact, sans-serif; font-weight: 400; font-size: 35px; line-height: 1; white-space: nowrap; }
  .booking-text { font-size: 16px; line-height: 21px; margin-top: 4px; }
  .booking-contact { margin-top: 42px; font-size: 17px; line-height: 22px; }
  .booking-contact p { margin-bottom: 22px; }

  .intro { position: absolute; left: 322px; top: 30px; width: 586px; }
  .intro-headline { font-family: "Bebas Neue", Impact, sans-serif; font-weight: 400; color: var(--green-text); font-size: 22.5px; line-height: 28px; letter-spacing: 0; }
  .intro-headline .lead { color: var(--orange); font-size: 38px; }
  .intro-body { font-size: 18px; line-height: 22px; margin-top: 4px; }
  .intro-body + .intro-body { margin-top: 22px; }

  .photo { position: absolute; left: 296px; top: 325px; width: 628px; height: 585px; background: linear-gradient(160deg, var(--photo-dark) 0%, var(--photo-mid) 55%, var(--photo-light) 100%); }
  .service-area { position: absolute; left: 24px; top: 18px; width: 590px; color: var(--white); font-size: 17px; line-height: 21px; }
  .service-area h3 { font-family: "Bebas Neue", Impact, sans-serif; font-weight: 400; font-size: 22px; line-height: 20px; }

  .notes { position: absolute; left: 316px; top: 922px; width: 594px; }
  .note { font-size: 15px; line-height: 19px; text-align: justify; margin-bottom: 20px; }
  .note-label { font-family: "Bebas Neue", Impact, sans-serif; font-weight: 400; color: var(--green-text); font-size: 24px; }
  .note-italic { font-style: italic; }
</style>
</head>
<body>
<main class="card">

  <header class="brand">
    <div class="brand-name"><span>Fairway</span><span>Relief</span><span>Rockets</span></div>
    <p class="brand-url">www.fairwayreliefrockets.com</p>
  </header>

  <section class="packages">
    <h2 class="packages-title"><span class="big">Several Packages</span><span class="small">to choose from</span></h2>
    <ul class="option-list">
      <li class="option"><svg viewBox="0 0 17 15"><path d="M1 8 L6 13 L16 1" fill="none" stroke="#fff" stroke-width="3"/></svg><span class="option-label">OPTION 1:</span> ($250 fee) $5 or $10 per player/per shot (player pays to participate)( player provides a ball)</li>
      <li class="option"><svg viewBox="0 0 17 15"><path d="M1 8 L6 13 L16 1" fill="none" stroke="#fff" stroke-width="3"/></svg><span class="option-label">Option 2:</span> ($500 fee - sponsor level) $5 or $10 per player/per shot and I provide all players a logo ball) 100% profit to the charity</li>
      <li class="option"><svg viewBox="0 0 17 15"><path d="M1 8 L6 13 L16 1" fill="none" stroke="#fff" stroke-width="3"/></svg><span class="option-label">Option 3:</span> ($500 fee - sponsor level) player participation is included in mulligan package price. 100% profit to the charity</li>
      <li class="option"><svg viewBox="0 0 17 15"><path d="M1 8 L6 13 L16 1" fill="none" stroke="#fff" stroke-width="3"/></svg><span class="option-label">Option 4:</span> Custom package design based upon charity requests</li>
    </ul>
  </section>

  <section class="booking">
    <h2 class="booking-title">Book Your Event Now</h2>
    <p class="booking-text">To book your date, please feel free to email me or call me.</p>
    <div class="booking-contact">
      <p>dale@fairwayreliefrockets.com</p>
      <p>&nbsp;555-014-2290</p>
      <p>www.fairwayreliefrockets.com</p>
    </div>
  </section>

  <section class="intro">
    <h1 class="intro-headline"><span class="lead">Are &nbsp;you tired or bored</span> of the same old challenges at every charity golf tournament? How about adding an exciting alternative to your typical golf tournament fundraising efforts by providing an RX-9 golf ball launcher.</h1>
    <p class="intro-body">Mulligans, longest drive, putting contests, &nbsp;Hole In One for a car? Yeah, you’ve been there and done that! Now it is time to add a new challenge?</p>
    <p class="intro-body">We set up on a par 4 or par 5 and your registered players will have the opportunity to use the rifle to launch their golf ball approximately 400 yards in place of driving off a tee.</p>
  </section>

  <section class="photo" role="img" aria-label="Photo of a golfer on a tee box firing the golf ball launcher in front of the pull-up event banner, trees and fairway behind">
    <div class="service-area">
      <h3>Currently serving:</h3>
      <p>Charlotte, Raleigh, Durham,Winston-Salem, Greensboro, Wilmington, Asheville &nbsp;Rock Hill SC, Greenville SC, Myrtle Beach SC, Atlanta, Pittsburgh</p>
    </div>
  </section>

  <section class="notes">
    <p class="note"><span class="note-label">Approval:</span> I request that the tournament director and the golf course clubhouse manager both acknowledge that they have approved of the use of the RX-9 golf ball launcher and are aware of the noise associated with it, and assume all liabilities beyond the teebox as they do for any other promotional event occurring on their course. (Ie- longest drive, hole in one, involving a participant teeing off.)</p>
    <p class="note note-italic"><span class="note-label">Collecting Funds:</span> I provide two options for collecting funds. The preferred method is to have players make a donation at the selected hole. The alternative is to accept credit cards via Clinkwell register at the hole for players who do not have cash but would like to make a donation anyways. Cash, tickets and Clinkwell totals are turned in after the final foursome fires away!</p>
  </section>

</main>
</body>
</html>
```